I need an amazing business card!

I am the principle in my own software company that develops zelPad and mobile applications. I require a great business card design. I've attached my corporate logo (Thanks Teodor!).
I would like the design to integrate the logo, my name, email address and skype account:
name Brent Halvorsen
email brenthalvorsen@tvekra.com
skype brenthalvorsen.net
I would like the back of the card to have a "write on me area" similar to the "write on me" card on this page, row 6:
http://us.plinkora.com/design-templates/business-cards/#industry=Computing%20%26%20IT
As far as the rest - it's all you!
Updates
1) Please add an example telephone number as well.
Industry/Entity Type
Software
Look and feel
Each slider illustrates characteristics of the customer's brand and the style your logo design should communicate.

```html
<!DOCTYPE html>
<html lang="en">
<head>
<meta charset="utf-8">
<title>Brent Halvorsen – Business Card</title>
<link rel="stylesheet" href="https://fonts.googleapis.com/css2?family=Exo+2:wght@300;400&family=Open+Sans:wght@700&family=Jura:wght@500&display=swap">
<style>
  :root {
    --page-bg: #e9e7e2;
    --card-dark: #1d2417;
    --card-mid: #3a4430;
    --accent: #a6c34c;
    --accent-soft: #b7d062;
    --white: #ffffff;
    --divider: rgba(255, 255, 255, 0.28);
    --panel: rgba(255, 255, 255, 0.09);
  }
  * { box-sizing: border-box; margin: 0; padding: 0; }
  html, body {
    width: 1200px;
    height: 1000px;
    overflow: hidden;
    background: var(--page-bg);
  }
  .canvas {
    position: relative;
    width: 1200px;
    height: 1000px;
  }
  .card {
    position: absolute;
    left: 280px;
    width: 640px;
    height: 380px;
    overflow: hidden;
    background:
      radial-gradient(ellipse 70% 75% at 45% 50%, var(--card-mid) 0%, var(--card-dark) 100%);
    box-shadow: 0 6px 18px rgba(0, 0, 0, 0.25);
  }
  .card--front { top: 90px; }
  .card--back { top: 530px; }

  /* Front */
  .brand {
    position: absolute;
    left: 48px;
    top: 128px;
    width: 160px;
    display: flex;
    flex-direction: column;
    align-items: center;
  }
  .brand__mark {
    width: 117px;
    height: 117px;
    border-radius: 22px;
    background: var(--accent);
  }
  .brand__name {
    margin-top: 16px;
    font-family: "Exo 2", sans-serif;
    font-weight: 400;
    font-size: 28px;
    letter-spacing: 14px;
    padding-left: 14px;
    color: var(--accent);
    line-height: 1;
  }
  .divider {
    position: absolute;
    left: 257px;
    top: 90px;
    width: 1px;
    height: 212px;
    background: var(--divider);
  }
  .contact-panel {
    position: absolute;
    left: 292px;
    top: 88px;
    width: 355px;
    height: 213px;
    background: var(--panel);
  }
  .contact-panel__name {
    position: absolute;
    left: 47px;
    top: 16px;
    font-family: "Open Sans", sans-serif;
    font-weight: 700;
    font-size: 27px;
    color: var(--accent);
  }
  .contact-list {
    position: absolute;
    left: 5px;
    top: 78px;
    list-style: none;
  }
  .contact-list__item {
    display: flex;
    align-items: center;
    height: 26px;
    margin-bottom: 24px;
  }
  .contact-list__icon {
    width: 26px;
    height: 26px;
    flex: none;
  }
  .contact-list__text {
    margin-left: 17px;
    font-family: "Exo 2", sans-serif;
    font-weight: 300;
    font-size: 16px;
    letter-spacing: 1.4px;
    color: var(--accent-soft);
  }

  /* Back */
  .back__watermark {
    position: absolute;
    left: 235px;
    top: 95px;
    width: 210px;
    height: 200px;
    border-radius: 36px;
    background: var(--accent);
    opacity: 0.12;
  }
  .back__prompt {
    position: absolute;
    left: 52px;
    top: 62px;
    font-family: "Jura", sans-serif;
    font-weight: 500;
    font-size: 21px;
    color: var(--accent);
  }
  .write-lines {
    position: absolute;
    left: 40px;
    top: 100px;
    width: 565px;
  }
  .write-lines__bar {
    height: 40px;
    margin-bottom: 32px;
    background: var(--white);
  }
</style>
</head>
<body>
<main class="canvas">

  <section class="card card--front" aria-label="Business card front">
    <div class="brand">
      <div class="brand__mark"></div>
      <div class="brand__name">tvekra</div>
    </div>

    <div class="divider"></div>

    <div class="contact-panel">
      <h1 class="contact-panel__name">Brent Halvorsen</h1>
      <ul class="contact-list">
        <li class="contact-list__item">
          <svg class="contact-list__icon" viewBox="0 0 26 26" aria-hidden="true">
            <circle cx="13" cy="13" r="13" fill="#fff"/>
            <rect x="6" y="8.5" width="14" height="9.5" fill="none" stroke="#1d2417" stroke-width="1.4"/>
            <path d="M6 8.5 L13 14 L20 8.5" fill="none" stroke="#1d2417" stroke-width="1.4"/>
          </svg>
          <span class="contact-list__text">brenthalvorsen@tvekra.com</span>
        </li>
        <li class="contact-list__item">
          <svg class="contact-list__icon" viewBox="0 0 26 26" aria-hidden="true">
            <circle cx="13" cy="13" r="13" fill="#fff"/>
          </svg>
          <span class="contact-list__text">brenthalvorsen.net</span>
        </li>
        <li class="contact-list__item">
          <svg class="contact-list__icon" viewBox="0 0 26 26" aria-hidden="true">
            <circle cx="13" cy="13" r="13" fill="#fff"/>
            <path d="M5.5 11 Q13 5 20.5 11 L18.5 12.5 L16.5 10.5 L9.5 10.5 L7.5 12.5 Z" fill="#1d2417"/>
            <rect x="8" y="12.5" width="10" height="6.5" rx="1" fill="#1d2417"/>
            <circle cx="13" cy="15.7" r="1.8" fill="#fff"/>
          </svg>
          <span class="contact-list__text">(555) 014-7392</span>
        </li>
      </ul>
    </div>
  </section>

  <section class="card card--back" aria-label="Business card back">
    <div class="back__watermark"></div>
    <p class="back__prompt">You can write one me</p>
    <div class="write-lines">
      <div class="write-lines__bar"></div>
      <div class="write-lines__bar"></div>
      <div class="write-lines__bar"></div>
      <div class="write-lines__bar"></div>
    </div>
  </section>

</main>
</body>
</html>
```